energy rating company

Web Design graphics and layout only

To create two pages for the website. First the home page and the second is the design for the job board for our clients use after login. I have attached files that explain in detail what the pages should have and the purpose/desires of each object. Please read these thoroughly.

The webpages need to be clean, professional, easy on the eye, obvious in all its buttons and functions with a strong call to action on the home page and branding and clean, great and obvious looking buttons and very simple but dynamic as well. We wish to be seen as contemporary.

Business Concept

Our business concept is simple, to build a website whereby our clients will be able to upload jobs for energy raters to quote on and subsequent complete the work if their quote is selected. To link energy ratings that are required with energy raters via our website. Similarly to the varlo website, jobs will be “advertised” on the job board and raters will select which jobs they wish to quote for.

I have attached a Word document explaining all the parts of the website and another word document showing what we are sort of after and a excel spreadsheet as well. Please read these in conjunction with this brief!
Updates

Dear All

I have submitted with my brief a word doc and excel spreadsheet of the two pages I want created.  However this is not the layout or design I want, I only put it together so that you will need to know what is required on each page.  Feel free to change and redesign it all.

Also the second page does not require the "process" logo or any other menu items except the first five being Home, How it works, About Us, testimonials and Contact us as per the home page.

We also are looking for something very professional and very clean.  It should be very easy to see exactly what you are looking for.

I will also extend the deadline for new designers!!  I am excited to see your talents!!

Thanks

I have increase budget and posted a note saying feel free to change all the details layout etc on my brief just include everything!!! 

Wanting a professional corporate look...

Want a professional corporate look

We have changed our minds and you we no longer require the process to be on the home page.

Thanks

Target Market(s)

Target Market

Home Inspection Companies
Pest Inspection Companies
Residential home buyers/sellers
Real Estate companies

Industry/Entity Type

It Company

Number of Pages Required

1 page

Requirements
Must have
• Colours and Styles

• The website should be mainly white as I believe it is seen as clean and simple with colour from the logos, but can be swayed if it projects the image we are after.

• It should be obvious and process orientated and I do believe symbols, pictures, etc should replace words where possible.

```html
<!DOCTYPE html>
<html lang="en">
<head>
<meta charset="utf-8">
<title>Ratewise Australia – Energy Rating Quotes</title>
<link href="https://fonts.googleapis.com/css2?family=Arimo:wght@400;700&display=swap" rel="stylesheet">
<style>
:root{
  --rust:#b5541a;
  --rust-text:#c25a1c;
  --green:#b7d60f;
  --green-light:#d2ea4a;
  --frame:#e4ebc4;
  --white:#ffffff;
  --ink:#111111;
  --grey:#8a8a8a;
  --field-border:#dcdcdc;
  --divider:#ece7c8;
}
*{box-sizing:border-box;margin:0;padding:0}
html,body{width:1200px;height:727px;overflow:hidden;background:var(--white)}
body{position:relative;font-family:"Arimo",Arial,sans-serif;color:var(--ink)}
.top-band{position:absolute;left:0;top:0;width:1200px;height:16px;background:var(--rust)}
.main-nav{position:absolute;left:552px;top:0;width:573px;height:47px;background:var(--rust);border-radius:0 0 14px 14px;display:flex;align-items:center;justify-content:space-around;padding:0 10px}
.main-nav a{color:var(--white);font-weight:700;font-size:14px;text-decoration:none;padding:0 14px;border-left:1px solid rgba(255,255,255,.8)}
.main-nav a:first-child{border-left:none}
.brand{position:absolute;left:84px;top:58px;display:flex;align-items:center;gap:14px}
.brand-dot{width:62px;height:62px;border-radius:50%;background:var(--rust)}
.brand-name{font-size:30px;font-weight:700;color:var(--rust)}
.action-tab{position:absolute;top:102px;height:53px;width:221px;border-radius:10px 10px 0 0;background:linear-gradient(var(--green-light) 0,var(--green) 45%);color:var(--white);font-weight:700;text-align:center;text-shadow:0 1px 1px rgba(0,0,0,.15)}
.action-icon{position:absolute;top:-34px;left:10px;width:44px;height:44px;border-radius:8px;z-index:0}
.tab-label{position:relative;z-index:1}
.tab-quote{left:423px}
.tab-quote .action-icon{background:linear-gradient(#f2f2f2,#b9b9b9)}
.tab-quote .tab-label{font-size:21px;line-height:53px;padding-left:40px}
.tab-raters{left:663px}
.tab-raters .action-icon{border-radius:50%;background:radial-gradient(circle at 35% 35%,#7fd0ff,#1569b8)}
.tab-raters .tab-label{font-size:20px;padding-top:10px;line-height:20px;padding-left:20px}
.tab-raters small{display:block;font-size:13px;line-height:18px}
.tab-board{left:904px}
.tab-board .action-icon{background:linear-gradient(135deg,#f3b51a,#3a9bd8 60%,#7bc043)}
.tab-board .tab-label{font-size:20px;line-height:21px;padding-top:10px;padding-left:24px}
.frame{position:absolute;left:53px;top:153px;width:1090px;height:541px;background:var(--frame);border-radius:10px}
.panel{position:absolute;background:var(--white);border-radius:9px}
.login{left:64px;top:165px;width:266px;height:223px;padding:10px 20px}
.panel-title{font-size:14px;font-weight:700;margin-bottom:13px}
.field-label{display:block;font-size:13px;margin-bottom:5px}
.field{display:block;width:224px;height:27px;border:1px solid var(--field-border);margin-bottom:16px}
.forgot{display:block;font-size:11px;font-weight:700;color:#e0201c;margin-top:-12px}
.login-actions{display:flex;justify-content:space-between;margin-top:15px}
.pill{width:96px;height:30px;border-radius:15px;background:linear-gradient(var(--green-light),var(--green));color:var(--white);font-weight:700;font-size:16px;display:flex;align-items:center;justify-content:center}
.testimonials{left:64px;top:398px;width:266px;height:288px;padding:10px 20px;overflow:hidden}
.testimonial{border-bottom:1px solid var(--divider);padding:8px 0 10px;width:212px}
.testimonial h3{font-size:13px;color:var(--rust-text);margin-bottom:2px}
.testimonial p{font-size:12.5px;line-height:14px}
.scrollbar{position:absolute;right:2px;top:3px;width:16px;height:282px;background:linear-gradient(90deg,#f4f4f4,#dcdcdc);border-radius:3px}
.scroll-thumb{position:absolute;left:2px;top:3px;width:12px;height:62px;border-radius:3px;background:linear-gradient(90deg,#9cc9f4,#3f86d8)}
.content{left:341px;top:165px;width:791px;height:521px;padding:22px 36px;color:var(--rust-text);font-size:14px;line-height:19px}
.content p{margin-bottom:19px}
.benefits{list-style:none;margin:0 0 19px 42px}
.benefits li::before{content:"•";margin-right:8px}
.footer{position:absolute;top:703px;left:64px;font-size:12.5px;color:var(--grey)}
</style>
</head>
<body>
<div class="top-band"></div>
<nav class="main-nav">
  <a href="#">Home</a><a href="#">How It Works</a><a href="#">About Us</a><a href="#">Testimonials</a><a href="#">Contact Us</a>
</nav>
<div class="brand"><span class="brand-dot"></span><span class="brand-name">Ratewise Australia</span></div>

<a class="action-tab tab-quote"><span class="action-icon" role="img" aria-label="Notepad and pencil icon"></span><div class="tab-label">GET A QUOTE</div></a>
<a class="action-tab tab-raters"><span class="action-icon" role="img" aria-label="Globe icon"></span><div class="tab-label">ENERGY RATERS<small>ADD YOUR BUSINESS</small></div></a>
<a class="action-tab tab-board"><span class="action-icon" role="img" aria-label="Shopping bags icon"></span><div class="tab-label">ACTIVE<br>JOB BOARD</div></a>

<div class="frame"></div>

<section class="panel login">
  <h2 class="panel-title">LOG IN</h2>
  <label class="field-label">Email Address</label><span class="field"></span>
  <label class="field-label">Password</label><span class="field"></span>
  <a class="forgot">Forgot your password?</a>
  <div class="login-actions"><span class="pill">SIGN UP</span><span class="pill">LOG IN</span></div>
</section>

<section class="panel testimonials">
  <h2 class="panel-title" style="margin-bottom:4px">CLIENT TESTIMONIALS</h2>
  <div class="testimonial"><h3>Client #1</h3><p>Eum ingenium pala et laoreet iriure usitas inhibeo ea consequat brevitas refoveo dignissim. Iusto mauris suscipere.</p></div>
  <div class="testimonial"><h3>Client #2</h3><p>Eum ingenium pala et laoreet iriure usitas inhibeo ea consequat brevitas refoveo dignissim. Iusto mauris suscipere.</p></div>
  <div class="testimonial"><h3>Client #3</h3><p>Eum ingenium pala et laoreet iriure usitas inhibeo ea consequat</p></div>
  <div class="scrollbar"><div class="scroll-thumb"></div></div>
</section>

<main class="panel content">
  <p>Ratewise Australia is Australia's leading professional energy rating consultancy firm specializing in large scaled residential and commercial energy rating logistics.</p>
  <p>We have professional and accredited energy raters in all States and Territories ready and waiting to provide quotes for and perform &nbsp;your energy rating jobs!</p>
  <p>It's Free, Fast and Easy to use and you get the best price and turnaround time that suits you!!</p>
  <p>Register with us, upload your job and specifications, and sit back and watch as energy raters provide quotes for your work!</p>
  <ul class="benefits">
    <li>Get the best priced quotes for your energy ratings</li>
    <li>Save time by listing a job to get many quotes</li>
    <li>Monitor your jobs and quotes on your own job board</li>
    <li>Be notified via email of all new quotes as they come in</li>
    <li>Be able to specify your desired turnaround times</li>
    <li>Accessible anytime and anywhere</li>
    <li>Choose a deadline for energy raters to supply quotes</li>
    <li>Have access to many qualified energy raters in your state all quoting for your work</li>
    <li>Be able to track your jobs and pay online</li>
    <li>Provide feedback on energy raters</li>
  </ul>
  <p>Its totally free to be registered with us and there is no obligations or hidden catches! &nbsp;So if you wish to utilise the amazing opportunity register now! &nbsp;This new website will be going live on the (insert date) so be ready to save some money!</p>
</main>

<footer class="footer">Copyright © 2010. Ratewise Australia. All rights reserved.</footer>
</body>
</html>
```